Poster for List of Company Values

We need a poster to outline our Values which will be displayed in our office as well as posted on our website and other platforms (so need to allow for some flexibly in its application).

File attached outlines what we currently have with design and also our company style guide.

Note that we are looking for a modern, clean look, which still represents our core activities of construction and environmental services.

You can also reference our website here:

https://quorvelgroup.com.au/

Happy to answer any questions you might have.

Thanks for your interest,
Brent

Target Market(s)

Internal and External clients

Industry/Entity Type

Construction, water and recycling

Font styles to use
Sans Serif

Requirements
Must have
• All values on the one page. Graphic to represent each value. Also needs to use company logo
Nice to have
• Preference for poster to be orientated in landscape
Should not have
• Do not follow example provided, this is only to demonstrate what we have to date and also the text required

```html
<!DOCTYPE html>
<html lang="en">
<head>
<meta charset="utf-8">
<title>Core Values – Quorvel Group</title>
<link rel="stylesheet" href="https://fonts.googleapis.com/css2?family=Carlito:wght@400;700&family=Open+Sans:wght@800&display=swap">
<style>
  :root {
    --ink: #3b3b3b;
    --body-ink: #333333;
    --paper: #ffffff;
    --map-tint: #f1f2f4;
    --loyal: #f7b21a;
    --loyal-deep: #b86f0c;
    --team: #ef5a3a;
    --team-deep: #8f2410;
    --open: #8cc152;
    --open-deep: #3f7a25;
    --initiative: #9b74c0;
    --initiative-deep: #5a3a8a;
    --respect: #4a86d4;
    --respect-deep: #1f3f96;
    --positive: #4cc3dc;
    --positive-deep: #1679a8;
    --brand-navy: #1e3a8a;
  }
  html, body {
    margin: 0;
    width: 1200px;
    height: 900px;
    overflow: hidden;
    background: var(--paper);
  }
  .poster { display: block; width: 1200px; height: 900px; }
  .headline {
    font-family: "Open Sans", sans-serif;
    font-weight: 800;
    fill: var(--ink);
  }
  .value-title {
    font-family: "Carlito", sans-serif;
    font-weight: 700;
    fill: var(--ink);
    text-anchor: middle;
    font-size: 45px;
  }
  .value-text {
    font-family: "Carlito", sans-serif;
    font-weight: 400;
    fill: var(--body-ink);
    text-anchor: middle;
    font-size: 21px;
  }
  .value-sub {
    font-family: "Carlito", sans-serif;
    font-weight: 700;
    fill: var(--body-ink);
    text-anchor: middle;
    font-size: 19px;
  }
  .brand-name {
    font-family: "Carlito", sans-serif;
    font-weight: 700;
    fill: var(--brand-navy);
    text-anchor: middle;
    font-size: 44px;
  }
  .web-address {
    font-family: "Carlito", sans-serif;
    fill: var(--ink);
    text-anchor: middle;
    font-size: 48px;
    letter-spacing: 7px;
  }
  .web-address .strong { font-weight: 700; }
  .link-line { fill: none; stroke-width: 7; stroke-linecap: round; }
  .hub-ring { fill: none; stroke-width: 8; }
  .icon { fill: none; stroke-width: 2.4; stroke-linecap: round; stroke-linejoin: round; }
</style>
</head>
<body>
<svg class="poster" viewBox="111 96 1778 1333" xmlns="http://www.w3.org/2000/svg">
  <defs>
    <linearGradient id="tile-face" x1="0" y1="0" x2="1" y2="1">
      <stop offset="0" stop-color="#ffffff"/>
      <stop offset="1" stop-color="#e6e7e9"/>
    </linearGradient>
    <radialGradient id="hub-face" cx="0.45" cy="0.4" r="0.7">
      <stop offset="0" stop-color="#ffffff"/>
      <stop offset="1" stop-color="#e4e5e7"/>
    </radialGradient>
    <linearGradient id="edge-loyal" x1="0" y1="0" x2="0" y2="1"><stop offset="0" stop-color="var(--loyal)"/><stop offset="1" stop-color="var(--loyal-deep)"/></linearGradient>
    <linearGradient id="edge-team" x1="0" y1="0" x2="0" y2="1"><stop offset="0" stop-color="var(--team)"/><stop offset="1" stop-color="var(--team-deep)"/></linearGradient>
    <linearGradient id="edge-open" x1="0" y1="0" x2="0" y2="1"><stop offset="0" stop-color="var(--open)"/><stop offset="1" stop-color="var(--open-deep)"/></linearGradient>
    <linearGradient id="edge-initiative" x1="0" y1="0" x2="0" y2="1"><stop offset="0" stop-color="var(--initiative)"/><stop offset="1" stop-color="var(--initiative-deep)"/></linearGradient>
    <linearGradient id="edge-respect" x1="0" y1="0" x2="0" y2="1"><stop offset="0" stop-color="var(--respect)"/><stop offset="1" stop-color="var(--respect-deep)"/></linearGradient>
    <linearGradient id="edge-positive" x1="0" y1="0" x2="0" y2="1"><stop offset="0" stop-color="var(--positive)"/><stop offset="1" stop-color="var(--positive-deep)"/></linearGradient>
    <filter id="lift" x="-30%" y="-30%" width="160%" height="170%">
      <feDropShadow dx="0" dy="14" stdDeviation="12" flood-color="#000" flood-opacity="0.22"/>
    </filter>
  </defs>

  <rect x="111" y="96" width="1778" height="1333" fill="var(--paper)"/>

  <rect x="240" y="360" width="1540" height="920" rx="200" fill="var(--map-tint)" opacity="0.6"
        role="img" aria-label="Faint world map in the background"/>

  <text class="headline" x="1000" y="340" font-size="206" text-anchor="middle" textLength="1450" lengthAdjust="spacingAndGlyphs">CORE VALUES</text>

  <g class="connectors">
    <path class="link-line" stroke="var(--loyal)" d="M975 640 V600 Q975 568 943 568 H860"/>
    <polygon fill="var(--loyal)" points="835,568 877,552 868,568 877,584"/>
    <path class="link-line" stroke="var(--initiative)" d="M1022 640 V600 Q1022 568 1054 568 H1135"/>
    <polygon fill="var(--initiative)" points="1160,568 1118,552 1127,568 1118,584"/>
    <path class="link-line" stroke="var(--team)" d="M835 805 H630"/>
    <polygon fill="var(--team)" points="598,805 664,789 654,805 664,821"/>
    <path class="link-line" stroke="var(--respect)" d="M1160 805 H1370"/>
    <polygon fill="var(--respect)" points="1398,805 1332,789 1342,805 1332,821"/>
    <path class="link-line" stroke="var(--open)" d="M975 970 V1010 Q975 1043 943 1043 H860"/>
    <polygon fill="var(--open)" points="835,1043 877,1027 868,1043 877,1059"/>
    <path class="link-line" stroke="var(--positive)" d="M1022 970 V1010 Q1022 1043 1054 1043 H1135"/>
    <polygon fill="var(--positive)" points="1160,1043 1118,1027 1127,1043 1118,1059"/>
  </g>

  <g class="hub">
    <path class="hub-ring" stroke="var(--initiative)" d="M1003.6 645.1 A160 160 0 0 1 1124.1 706.5"/>
    <path class="hub-ring" stroke="var(--respect)" d="M1130.6 715.5 A160 160 0 0 1 1127.4 899.0"/>
    <path class="hub-ring" stroke="var(--positive)" d="M1120.6 907.9 A160 160 0 0 1 1003.6 964.9"/>
    <path class="hub-ring" stroke="var(--open)" d="M992.4 964.9 A160 160 0 0 1 875.4 907.9"/>
    <path class="hub-ring" stroke="var(--team)" d="M868.6 899.1 A160 160 0 0 1 868.6 710.9"/>
    <path class="hub-ring" stroke="var(--loyal)" d="M875.4 702.2 A160 160 0 0 1 992.4 645.1"/>
    <circle cx="998" cy="805" r="130" fill="url(#hub-face)" filter="url(#lift)"/>
    <text class="brand-name" x="998" y="820">quorvel</text>
  </g>

  <g class="value value-loyal">
    <rect x="-138" y="-138" width="276" height="276" rx="30" fill="url(#edge-loyal)" transform="translate(615 567) scale(1 0.72) rotate(45)"/>
    <rect x="-127" y="-127" width="254" height="254" rx="26" fill="url(#tile-face)" filter="url(#lift)" transform="translate(615 570) rotate(45)"/>
    <path class="icon" stroke="var(--loyal)" d="M622 478 C604 466 606 450 616 450 C620 450 622 454 622 456 C622 454 624 450 628 450 C638 450 640 466 622 478 Z M586 482 H598 V504 H586 Z M598 488 H618 Q626 488 626 494 H610 M598 500 H628 L650 488"/>
    <text class="value-title" x="618" y="555">be LOYAL</text>
    <text class="value-text" x="618" y="588">We take care of our own</text>
    <text class="value-text" x="618" y="609">and provide opportunities</text>
    <text class="value-text" x="618" y="630">to listen and support</text>
    <text class="value-text" x="618" y="651">each other.</text>
  </g>

  <g class="value value-team">
    <rect x="-138" y="-138" width="276" height="276" rx="30" fill="url(#edge-team)" transform="translate(377 802) scale(1 0.72) rotate(45)"/>
    <rect x="-127" y="-127" width="254" height="254" rx="26" fill="url(#tile-face)" filter="url(#lift)" transform="translate(377 805) rotate(45)"/>
    <g class="icon" stroke="var(--team)">
      <circle cx="368" cy="710" r="12"/><circle cx="384" cy="710" r="12"/>
      <path d="M356 684 l-4 -6 M376 680 v-6 M396 684 l4 -6"/>
    </g>
    <text class="value-title" x="377" y="790">think TEAM</text>
    <text class="value-text" x="382" y="824">We communicate effectively</text>
    <text class="value-text" x="382" y="845">and work as a team by helping</text>
    <text class="value-text" x="382" y="866">and supporting</text>
    <text class="value-text" x="382" y="887">each other.</text>
  </g>

  <g class="value value-open">
    <rect x="-138" y="-138" width="276" height="276" rx="30" fill="url(#edge-open)" transform="translate(615 1042) scale(1 0.72) rotate(45)"/>
    <rect x="-127" y="-127" width="254" height="254" rx="26" fill="url(#tile-face)" filter="url(#lift)" transform="translate(615 1045) rotate(45)"/>
    <path class="icon" stroke="var(--open)" d="M618 944 C600 932 602 918 611 918 C615 918 618 922 618 924 C618 922 621 918 625 918 C634 918 636 932 618 944 Z M596 930 Q592 950 610 962 M640 930 Q644 950 626 962"/>
    <text class="value-title" x="608" y="1012">be OPEN</text>
    <text class="value-title" x="613" y="1055">and HONEST</text>
    <text class="value-text" x="614" y="1081">We are clear and open with</text>
    <text class="value-text" x="614" y="1102">each other, and provide</text>
    <text class="value-text" x="614" y="1123">an approachable and</text>
    <text class="value-text" x="614" y="1144">friendly</text>
    <text class="value-text" x="614" y="1165">environment.</text>
  </g>

  <g class="value value-initiative">
    <rect x="-138" y="-138" width="276" height="276" rx="30" fill="url(#edge-initiative)" transform="translate(1382 567) scale(1 0.72) rotate(45)"/>
    <rect x="-127" y="-127" width="254" height="254" rx="26" fill="url(#tile-face)" filter="url(#lift)" transform="translate(1382 570) rotate(45)"/>
    <g class="icon" stroke="var(--initiative)">
      <circle cx="1388" cy="454" r="12"/>
      <path d="M1383 466 v8 h10 v-8 M1384 480 h8 M1388 434 v-4 M1406 454 h4 M1366 454 h4"/>
    </g>
    <text class="value-title" x="1378" y="533">show</text>
    <text class="value-title" x="1378" y="574">INITIATIVE</text>
    <text class="value-text" x="1384" y="607">We celebrate and recognize</text>
    <text class="value-text" x="1384" y="628">our own and encourage</text>
    <text class="value-text" x="1384" y="649">forward thinking.</text>
  </g>

  <g class="value value-respect">
    <rect x="-138" y="-138" width="276" height="276" rx="30" fill="url(#edge-respect)" transform="translate(1627 802) scale(1 0.72) rotate(45)"/>
    <rect x="-127" y="-127" width="254" height="254" rx="26" fill="url(#tile-face)" filter="url(#lift)" transform="translate(1627 805) rotate(45)"/>
    <g class="icon" stroke="var(--respect)">
      <circle cx="1616" cy="702" r="16"/><circle cx="1638" cy="702" r="16"/>
    </g>
    <text class="value-title" x="1618" y="772">show</text>
    <text class="value-title" x="1623" y="814">RESPECT</text>
    <text class="value-text" x="1625" y="844">We value the diversity</text>
    <text class="value-text" x="1625" y="865">and opinions of all.</text>
  </g>

  <g class="value value-positive">
    <rect x="-138" y="-138" width="276" height="276" rx="30" fill="url(#edge-positive)" transform="translate(1382 1042) scale(1 0.72) rotate(45)"/>
    <rect x="-127" y="-127" width="254" height="254" rx="26" fill="url(#tile-face)" filter="url(#lift)" transform="translate(1382 1045) rotate(45)"/>
    <g class="icon" stroke="var(--positive)">
      <circle cx="1383" cy="950" r="30"/>
      <path d="M1368 951 L1379 962 L1399 938"/>
    </g>
    <text class="value-title" x="1384" y="1030">be POSITIVE</text>
    <text class="value-sub" x="1381" y="1060">SMILE</text>
    <text class="value-text" x="1381" y="1081">We are solutions focused</text>
    <text class="value-text" x="1381" y="1102">and encourage a positive</text>
    <text class="value-text" x="1381" y="1123">attitude turning a</text>
    <text class="value-text" x="1381" y="1144">negative into</text>
    <text class="value-text" x="1381" y="1165">a positive.</text>
  </g>

  <text class="web-address" x="987" y="1286">www.<tspan class="strong">quorvelgroup</tspan>.com</text>
</svg>
</body>
</html>
```